Plakat-Design für Bio-Hofkäserei
Zielgruppe
Wir sind eine Hofkäserei in Südtirol (www.lerchbodenhof.it), das Werbeplakat soll an einem Wanderweg in unserer Ortschaft angebracht werden und Kunden über den Hofladen und die Käsesorten informieren (ca. 50 m Entfernung zum Hofladen). Es sollte nur die Hofkäserei mit Hofladen und Käsesorten beworben werden, weniger die restlichen Produkte und Dienstleistungen unseres Betriebs.
Unsere Produktetiketten werden schnellstmöglich online gestellt, damit Sie sich daran orientieren können.
Aufgabenstellung
Hochformat, Text auf deutsch und italienisch, z.B: 'in unserer bio-Hofkäserei finden Sie edlen Rohmilchkäse aus Kuh-, Ziegen- und Schafmilch' - 'Nel nostro caseificio biologico potete trovare pregiati formaggi a latte crudo di mucca, capra e pecora'.
Wiedererkennbarkeit mit unseren Produktetiketten wären wünschenswert.
Hochauflösende Bilder werden in einem späteren Schritt zur Verfügung gestellt, vorerst können Bilder unserer Homepage verwendet werden.

```html
<!DOCTYPE html>
<html lang="de">
<head>
<meta charset="utf-8">
<title>Lerchbodenhof – Plakat Hofkäserei</title>
<link href="https://fonts.googleapis.com/css2?family=Satisfy&family=Jost:wght@400;500&display=swap" rel="stylesheet">
<style>
  :root {
    --page: #ececea;
    --paper: #ffffff;
    --stone: #c5bdb3;
    --green: #95c11f;
    --green-pale: #e4efc4;
    --ink: #1d1d1b;
    --wood-dark: #5e4330;
    --wood: #7d5d40;
    --cheese: #dccb9f;
    --cheese-pale: #ece2c6;
  }
  * { box-sizing: border-box; margin: 0; padding: 0; }
  html, body { width: 1200px; height: 1200px; overflow: hidden; }
  body {
    background: var(--page);
    font-family: "Jost", sans-serif;
    color: var(--ink);
    display: flex;
    align-items: center;
    justify-content: center;
  }
  .poster {
    position: relative;
    width: 800px;
    height: 1130px;
    background: var(--paper);
    box-shadow: 0 6px 18px rgba(0,0,0,0.18);
    overflow: hidden;
  }
  .poster__head {
    position: absolute;
    left: 0; top: 0;
    width: 800px; height: 295px;
  }
  .poster__head svg { display: block; }
  .brand {
    position: absolute;
    left: 0; right: 0; top: 222px;
    text-align: center;
    color: var(--paper);
    font-weight: 400;
    font-size: 30px;
    letter-spacing: 0.16em;
    text-transform: uppercase;
  }
  .animals {
    position: absolute;
    left: 0; top: 318px;
    width: 800px; height: 86px;
  }
  .animal {
    position: absolute;
    top: 0;
    width: 90px; height: 84px;
    background: radial-gradient(circle at 50% 45%, var(--green) 0%, #b7d65c 55%, var(--green-pale) 100%);
    border-radius: 10px;
  }
  .animal--cow { left: 34px; }
  .animal--goat { left: 355px; }
  .animal--sheep { left: 676px; }
  .headline {
    position: absolute;
    left: 0; top: 428px;
    width: 800px; height: 177px;
    background: var(--green);
    color: var(--paper);
    font-family: "Satisfy", cursive;
    font-weight: 400;
    text-align: center;
    padding-top: 16px;
  }
  .headline__de { font-size: 60px; line-height: 76px; font-weight: 400; }
  .headline__it { font-size: 45px; line-height: 60px; font-weight: 400; }
  .intro {
    position: absolute;
    left: 28px; top: 620px;
    font-size: 23px;
    line-height: 31px;
    text-transform: uppercase;
    letter-spacing: 0.02em;
  }
  .intro p + p { margin-top: 10px; }
  .intro em { font-style: normal; color: var(--green); }
  .cheese-photo {
    position: absolute;
    left: 0; top: 770px;
    width: 800px; height: 208px;
    background: linear-gradient(180deg, var(--wood-dark) 0%, var(--wood) 22%, var(--cheese) 45%, var(--cheese-pale) 62%, var(--wood) 85%, #9b7550 100%);
  }
  .footer {
    position: absolute;
    left: 0; top: 995px;
    width: 800px; height: 100px;
  }
  .contact {
    position: absolute;
    left: 36px; top: 4px;
    font-style: normal;
    font-size: 13px;
    line-height: 17px;
    text-transform: uppercase;
    letter-spacing: 0.03em;
  }
  .contact__web { margin-top: 12px; }
  .farm-photo {
    position: absolute;
    left: 258px; top: 2px;
    width: 140px; height: 86px;
    background: linear-gradient(180deg, #8fa7bd 0%, #b9a48a 45%, #6f8f45 100%);
  }
  .bio-badge {
    position: absolute;
    left: 398px; top: 2px;
    width: 133px; height: 86px;
    background: var(--green);
  }
  .distance {
    position: absolute;
    left: 555px; top: 0;
    color: var(--green);
    font-family: "Satisfy", cursive;
    font-size: 38px;
    line-height: 44px;
  }
  .distance__arrow {
    position: absolute;
    left: 738px; top: 10px;
  }
</style>
</head>
<body>
  <main class="poster">
    <header class="poster__head">
      <svg width="800" height="295" viewBox="0 0 800 295" aria-hidden="true">
        <path d="M0 115 Q400 -40 800 115 L800 295 L0 295 Z" fill="var(--stone)"/>
      </svg>
      <div class="brand">Lerchbodenhof</div>
    </header>

    <section class="animals">
      <div class="animal animal--cow" role="img" aria-label="Kuhkopf-Piktogramm in Grün"></div>
      <div class="animal animal--goat" role="img" aria-label="Ziegenkopf-Piktogramm in Grün"></div>
      <div class="animal animal--sheep" role="img" aria-label="Schafkopf-Piktogramm in Grün"></div>
    </section>

    <section class="headline">
      <h1 class="headline__de">Bio Hofkäserei mit Hofladen</h1>
      <h2 class="headline__it">Caseificio Biologico con vendita diretta</h2>
    </section>

    <section class="intro">
      <p>In unserer Bio-Hofkäserei finden Sie<br>edlen Rohmilchkäse aus <em>Kuh-, Ziegen- und Schafmilch.</em></p>
      <p>Nel nostro caseificio biologico potete trovare<br>pregiati formaggi a latte crudo di <em>mucca, capra e peco.</em></p>
    </section>

    <div class="cheese-photo" role="img" aria-label="Foto: vier Rohmilchkäselaibe mit Etiketten auf einem Holzbrett"></div>

    <footer class="footer">
      <address class="contact">
        Familie Anton Rainalter<br>
        Bodenweg 7 &nbsp;&nbsp;39020 Hochtal<br>
        Obervinschgau
        <div class="contact__web">www.lerchbodenhof.it<br>Tel. +39 0473 612 450</div>
      </address>
      <div class="farm-photo" role="img" aria-label="Foto: Bauernhof mit Hofladen vor Bergkulisse"></div>
      <div class="bio-badge" role="img" aria-label="Bio-Zertifikatssiegel"></div>
      <div class="distance">nur noch<br>50 Meter</div>
      <svg class="distance__arrow" width="30" height="62" viewBox="0 0 30 62" aria-hidden="true">
        <path d="M0 0 L30 31 L0 62 Z" fill="var(--green)"/>
      </svg>
    </footer>
  </main>
</body>
</html>
```